Charity website needing new website design

Hi there. We are looking to get a revamped website for our non for profit charity. We specialise in eye cataract surgeries and ear care around the world. Please visit our website brightcareaid.org.au for the current layout.
I have attached a brief with photos. The about us page please include an interactive map showing our locations we operate in. The website should be easy to use, match our logo design and be clear to navigate. Pixvault and other images can be used if they fit the scheme of the website and feel. The donation page should incorporate the gateway to receive donations. The team page should have each photo of the team member next to it. Please compare to other charity websites such as ORANTA, Global Haven etc. Another website which has a lovely and easy to use scheme is tkqhaustralia.org.au
The tabs should be in the following order:
About us, Why Health? Our Team, Eye Care Programs, Ear Care Programs, Contact Us, Donate.
Please make sure the website is both compatible with mobile & computer.
The Listed Benefactor Badge can be at the footer of the page with details of brightcare etc

```html
<!DOCTYPE html>
<html lang="en">
<head>
<meta charset="utf-8">
<title>Brightcare Aid Foundation</title>
<link href="https://fonts.googleapis.com/css2?family=Montserrat:wght@400;500;600;700&display=swap" rel="stylesheet">
<style>
  :root{
    --navy:#0e4a63;
    --teal:#2f6f88;
    --teal-dark:#1d4f68;
    --green:#7aa13c;
    --orange:#f2a93b;
    --text:#4a4a4a;
    --white:#ffffff;
    --line:#9aa9b0;
  }
  *{box-sizing:border-box;margin:0;padding:0}
  html,body{width:1200px;height:4090px;overflow:hidden}
  body{font-family:"Montserrat",sans-serif;color:var(--text);background:var(--white);position:relative}
  .abs{position:absolute}
  .btn{position:absolute;background:var(--green);color:var(--white);font-size:15px;font-weight:500;display:flex;align-items:center;justify-content:center;width:137px;height:38px}
  .section-title{color:var(--navy);font-weight:700;font-size:41px;line-height:1.2}

  /* header */
  .site-header{left:0;top:0;width:1200px;height:60px;background:var(--white);z-index:3}
  .brand-tab{left:127px;top:0;width:254px;height:95px;z-index:4}
  .brand-name{left:150px;top:26px;width:210px;text-align:center;z-index:5;color:var(--navy);font-weight:700;font-size:17px;line-height:1.1}
  .brand-name small{display:block;font-size:12px;font-weight:600;letter-spacing:1px}
  .main-nav{left:444px;top:21px;width:645px;display:flex;justify-content:space-between;font-size:14px;color:#222;z-index:5}

  /* hero */
  .hero{left:0;top:60px;width:1200px;height:556px;background:linear-gradient(110deg,#2c6e87 0%,#2f7590 55%,#3d8199 100%)}
  .hero-title{left:111px;top:170px;color:var(--white);font-weight:700;font-size:46px;line-height:51px;width:560px}
  .hero-text{left:111px;top:353px;color:var(--white);font-size:13.5px;letter-spacing:-.2px;line-height:26px;width:545px}

  /* about */
  .photo{position:absolute}
  .about-title{left:697px;top:738px}
  .about-text{left:697px;top:806px;width:400px;font-size:13.5px;letter-spacing:-.1px;line-height:23.2px}
  .mark{left:444px;top:706px;width:178px;height:159px;display:flex;flex-direction:column;align-items:center;justify-content:center;gap:10px;color:var(--navy);font-weight:700;font-size:16px}
  .mark span.dot{width:70px;height:70px;border-radius:50%;background:var(--green)}

  /* specialise */
  .specialise{left:0;top:1193px;width:1200px;height:648px;background:linear-gradient(180deg,#3a7a93 0%,#2f6f88 60%,#2b6a83 100%)}
  .spec-title{left:0;top:1270px;width:1200px;text-align:center;color:var(--white);font-weight:700;font-size:41px}
  .card-label{position:absolute;height:60px;width:310px;background:var(--orange);color:var(--white);font-weight:600;font-size:23px;display:flex;align-items:center;justify-content:center;top:1627px}

  /* why */
  .why-title{left:114px;top:1950px}
  .why-text{left:114px;top:2018px;width:420px;font-size:13.5px;letter-spacing:-.2px;line-height:22.8px;text-align:justify}
  .why-text p+p{margin-top:10px}

  /* cta */
  .cta{left:0;top:2460px;width:1200px;height:465px;background:radial-gradient(ellipse at 50% 70%,#2c5f7c 0%,#1c4a66 60%,#17405a 100%)}
  .cta-kicker{left:0;top:2618px;width:1200px;text-align:center;color:var(--white);font-weight:600;font-size:26px}
  .cta-title{left:0;top:2662px;width:1200px;text-align:center;color:var(--white);font-weight:700;font-size:40px}

  /* trusted */
  .trusted-title{left:0;top:3002px;width:1200px;text-align:center}
  .supporters{left:119px;top:3088px;width:970px;display:flex;justify-content:space-between}
  .supporters span{width:70px;height:70px;border-radius:50%;background:linear-gradient(160deg,#c9b7a4,#6b5a50)}

  /* newsletter */
  .news-mark{left:95px;top:3261px;width:513px;height:461px;display:flex;flex-direction:column;align-items:center;justify-content:center;gap:26px;color:var(--navy);font-weight:700;font-size:30px}
  .news-mark .dot{width:240px;height:240px;border-radius:50%;background:linear-gradient(160deg,#8bb44a,#1d5a74)}
  .news-title{left:641px;top:3244px}
  .field{position:absolute;left:641px;width:448px;height:38px;border:1px solid #555;font-size:16px;color:#333;padding:8px 20px}

  /* footer */
  .site-footer{left:0;top:3817px;width:1200px;height:273px;background:linear-gradient(180deg,#23607c 0%,#1e5a75 100%)}
  .footer-brand{left:0;top:3905px;width:1200px;text-align:center;color:var(--white);font-weight:700;font-size:28px;line-height:1}
  .footer-brand small{display:block;font-size:17px;font-weight:600;letter-spacing:1px;margin-top:3px}
  .footer-nav{left:0;top:3988px;width:1200px;display:flex;justify-content:center;gap:14px;color:var(--white);font-size:14px}
  .footer-rule{left:111px;top:4028px;width:978px;height:1px;background:var(--line)}
  .copyright{left:0;top:4046px;width:1200px;text-align:center;color:var(--white);font-size:13.5px}
</style>
</head>
<body>

<header>
  <div class="abs site-header"></div>
  <svg class="abs brand-tab" viewBox="0 0 254 95" aria-hidden="true"><polygon points="0,0 254,0 254,60 224,95 30,95 0,60" fill="#fff" stroke="#e6e6e6"/></svg>
  <div class="abs brand-name">BRIGHTCARE AID<small>FOUNDATION</small></div>
  <nav class="abs main-nav">
    <span>About us</span><span>Why Health?</span><span>Our Team</span><span>Eye Care Programs</span><span>Ear Care Programs</span><span>Contact Us</span>
  </nav>
</header>

<section>
  <div class="abs hero" role="img" aria-label="Hands reaching toward each other, tinted teal"></div>
  <h1 class="abs hero-title">Help Bring Basic Health Care To Every Person On The Planet.</h1>
  <p class="abs hero-text">Through symbiotic health programs brightcare aid foundation provides innovative solutions to Eye and Hearing Health in the developing world with an ethical professional and sustainable approach.</p>
  <div class="btn" style="left:111px;top:447px">Donate</div>
</section>

<section>
  <div class="photo" style="left:111px;top:706px;width:308px;height:311px;background:linear-gradient(160deg,#9a958d,#5e5a55)" role="img" aria-label="Person on a street holding a cardboard sign asking for help"></div>
  <div class="abs mark"><span class="dot"></span>Brightcare</div>
  <div class="photo" style="left:322px;top:879px;width:335px;height:224px;background:linear-gradient(150deg,#8a5a3a,#3a2418);border:2px solid #fff" role="img" aria-label="Cupped dusty hands held open"></div>
  <h2 class="abs section-title about-title">About Us</h2>
  <p class="abs about-text">With over 70 years of humanitarian aid experience across our members collectively. United in our passion we established brightcare aid foundation to provide innovative, sustainable, ethical and professional ymbiotic solutions across health programs focussing on restorative eyesight and hearing procedures. We brightcare quality healthcare and improvement of general health and wellbeing coupled with treating and preventing other health conditions.</p>
  <div class="btn" style="left:697px;top:1028px">Learn More</div>
</section>

<section>
  <div class="abs specialise" role="img" aria-label="Faint photo of a health worker with a patient, tinted teal"></div>
  <h2 class="abs spec-title">We Are Specialise</h2>
  <div class="photo" style="left:111px;top:1365px;width:310px;height:254px;background:linear-gradient(150deg,#d8d4cf,#6d7275)" role="img" aria-label="Eye examination with an ophthalmic lens"></div>
  <div class="photo" style="left:444px;top:1365px;width:310px;height:254px;background:linear-gradient(150deg,#a7a59a,#3f4a45)" role="img" aria-label="Health worker checking a patient outdoors"></div>
  <div class="photo" style="left:778px;top:1365px;width:310px;height:254px;background:linear-gradient(150deg,#d9b47a,#7a5a3a)" role="img" aria-label="Doctor caring for a young child"></div>
  <div class="card-label" style="left:111px">Eye Care</div>
  <div class="card-label" style="left:444px">Ear Care</div>
  <div class="card-label" style="left:778px">General Health</div>
  <div class="btn" style="left:531px;top:1716px">Donate</div>
</section>

<section>
  <h2 class="abs section-title why-title">Why Health?</h2>
  <div class="abs why-text">
    <p>Charities often focus on the last component of aid, which is at times critically required without focusing on the root cause of poverty. Brightcare Aid Foundation focuses on the fundamental factors of poverty through providing health programs such as preventable blindness operations and hearing loss restoration.</p>
    <p>By restoring health and vital senses, it enables adults the ability to work and provide for the households whilst children gain the capacity to go to school and have a more fruitful childhood. In turn this improves the livelihoods of patients and creates a more productive society.</p>
  </div>
  <div class="btn" style="left:114px;top:2305px">Learn More</div>
  <div class="photo" style="left:640px;top:1925px;width:450px;height:450px;border-radius:50%;background:linear-gradient(150deg,#d9c9c6,#4f7fa8 70%,#2f5f8f);box-shadow:0 8px 14px rgba(0,0,0,.35)" role="img" aria-label="Surgeon performing eye surgery with an operating microscope"></div>
</section>

<section>
  <div class="abs cta" role="img" aria-label="Close-up of cupped hands holding water, tinted dark blue"></div>
  <p class="abs cta-kicker">Brightcare Gifting Vision</p>
  <h2 class="abs cta-title">Learn About Brightcare Aid Foundation</h2>
  <div class="btn" style="left:531px;top:2727px">Donate</div>
</section>

<section>
  <h2 class="abs section-title trusted-title">Trusted By Those You Trust</h2>
  <div class="abs supporters" role="img" aria-label="Portrait photos of twelve supporters">
    <span></span><span></span><span></span><span></span><span></span><span></span><span></span><span></span><span></span><span></span><span></span><span></span>
  </div>
</section>

<section>
  <div class="abs news-mark"><span class="dot"></span>Brightcare Aid Foundation</div>
  <h2 class="abs section-title news-title">Sign Up<br>To Our Newsletter</h2>
  <div class="field" style="top:3371px">Full Name</div>
  <div class="field" style="top:3431px">Email Address</div>
  <div class="field" style="top:3491px">Phone Number</div>
  <div class="field" style="top:3552px;height:114px">Message Here....</div>
  <div class="btn" style="left:641px;top:3687px;width:167px">Submit</div>
</section>

<footer>
  <div class="abs site-footer"></div>
  <div class="abs footer-brand">BRIGHTCARE AID<small>FOUNDATION</small></div>
  <nav class="abs footer-nav">
    <span>About us</span><span>Why Health?</span><span>Our Team</span><span>Eye Care Programs</span><span>Ear Care Programs</span><span>Contact Us</span>
  </nav>
  <div class="abs footer-rule"></div>
  <p class="abs copyright">2024 © Copyright, Brightcare Aid Foundation. All rights reserved.</p>
</footer>

</body>
</html>
```